We are a building company that build new homes and units we are looking for something fresh and looks good my company name is
Orland Building Group Pty Ltd

Industry/Entity Type

Building

Contact Information for Business Card

Name Marco Deluca-Finn
Tittle: Director
Address 14 Larkmoor St. Pellingwood Vic 3091
Ph: 03 9512 4386
Mobile : 0400 736 294

www.orlandbuildinggroup.com.au
Email: sales@orlandbuildinggroup.com.au

```html
<!DOCTYPE html>
<html lang="en">
<head>
<meta charset="utf-8">
<title>Orland Building Group Pty Ltd – Business Card</title>
<link rel="stylesheet" href="https://fonts.googleapis.com/css2?family=Arimo:wght@400;700&display=swap">
<style>
  :root {
    --navy: #201e5a;
    --band: #cccbdc;
    --white: #ffffff;
    --frame: #c9c9cf;
    --ink: #111111;
    --page: #f2f0ec;
  }
  * { box-sizing: border-box; margin: 0; padding: 0; }
  html, body { width: 1189px; height: 1200px; overflow: hidden; }
  body {
    background: var(--page);
    font-family: "Arimo", Arial, sans-serif;
    position: relative;
  }
  .card {
    position: absolute;
    left: 166px;
    width: 856px;
    height: 488px;
    overflow: hidden;
    box-shadow: 6px 8px 10px rgba(0,0,0,0.25);
  }
  .card-front { top: 67px; background: var(--white); }
  .card-back { top: 627px; background: var(--navy); }

  .company {
    position: absolute; top: 34px; left: 0; right: 0;
    text-align: center; color: var(--navy);
    font-weight: 700; font-size: 42px; line-height: 50px;
    letter-spacing: 0.3px; white-space: nowrap;
  }
  .person {
    position: absolute; top: 88px; left: 0; right: 0;
    text-align: center; color: var(--navy);
    font-weight: 700; font-size: 31px; line-height: 38px;
    white-space: nowrap;
  }
  .phones {
    position: absolute; top: 130px; left: 0; right: 0;
    display: flex; justify-content: center; gap: 48px;
    font-weight: 700; font-size: 26px; line-height: 32px;
    color: var(--ink); white-space: nowrap;
  }
  .phone { display: flex; align-items: center; gap: 10px; }
  .phone svg { fill: var(--navy); }
  .grey-band {
    position: absolute; top: 165px; left: 0; right: 0; height: 20px;
    background: var(--band);
  }
  .gallery {
    position: absolute; top: 197px; left: 10px; right: 10px; height: 213px;
    display: flex; justify-content: space-between;
  }
  .photo-frame {
    width: 198px; height: 213px;
    border: 1px solid var(--frame);
    padding: 12px;
    background: var(--white);
  }
  .photo { width: 100%; height: 100%; }
  .photo-exterior-1 { background: linear-gradient(180deg, #c9cdd6 0%, #8e8a86 55%, #5e6a45 100%); }
  .photo-exterior-2 { background: linear-gradient(180deg, #2f6fb3 0%, #8a6a52 45%, #4f8a2a 75%, #2e6a1c 100%); }
  .photo-interior { background: linear-gradient(180deg, #e9ecea 0%, #b9a58c 60%, #d9d6d2 100%); }
  .photo-pool { background: linear-gradient(180deg, #8a6a3a 0%, #5a3f22 55%, #1d2430 100%); }
  .front-footer {
    position: absolute; left: 0; right: 0; bottom: 0; height: 65px;
    background: var(--navy); color: var(--white);
    display: flex; align-items: center; justify-content: center;
    font-size: 23px; white-space: nowrap;
  }
  .divider {
    display: inline-block; width: 2px; height: 32px;
    background: var(--white); margin: 0 14px;
  }
  .back-rule {
    position: absolute; top: 240px; left: 0; right: 0; height: 2px;
    background: var(--white);
  }
  .back-url {
    position: absolute; top: 220px; left: 0; right: 0;
    text-align: center; font-size: 31px; line-height: 42px;
    color: var(--white); white-space: nowrap;
  }
  .back-url span { background: var(--navy); padding: 0 10px; }
</style>
</head>
<body>
  <section class="card card-front">
    <h1 class="company">ORLAND BUILDING GROUP PTY LTD</h1>
    <p class="person">Marco Deluca-Finn</p>
    <div class="phones">
      <span class="phone">
        <svg width="11" height="20" viewBox="0 0 11 20" aria-hidden="true"><rect x="0" y="3" width="11" height="17" rx="2"/><rect x="7" y="0" width="2" height="4"/><rect x="2" y="5" width="7" height="4" fill="#fff"/><g fill="#fff"><rect x="2" y="11" width="2" height="2"/><rect x="5" y="11" width="2" height="2"/><rect x="2" y="14" width="2" height="2"/><rect x="5" y="14" width="2" height="2"/></g></svg>
        0400 736 294
      </span>
      <span class="phone">
        <svg width="28" height="20" viewBox="0 0 28 20" aria-hidden="true"><path d="M1 6 C5 0 23 0 27 6 L24 9 L19 7 L19 4 C15 3 13 3 9 4 L9 7 L4 9 Z"/><path d="M8 9 L20 9 L24 19 L4 19 Z"/><circle cx="14" cy="14" r="3" fill="#fff"/></svg>
        03 9512 4386
      </span>
    </div>
    <div class="grey-band"></div>
    <div class="gallery">
      <div class="photo-frame"><div class="photo photo-exterior-1" role="img" aria-label="Photo of a modern angular timber-screened home at dusk"></div></div>
      <div class="photo-frame"><div class="photo photo-exterior-2" role="img" aria-label="Photo of a contemporary two-storey house with lawn"></div></div>
      <div class="photo-frame"><div class="photo photo-interior" role="img" aria-label="Photo of a bright kitchen and dining area"></div></div>
      <div class="photo-frame"><div class="photo photo-pool" role="img" aria-label="Photo of a bedroom opening onto a pool at night"></div></div>
    </div>
    <div class="front-footer">
      www.orlandbuildinggroup.com.au<span class="divider"></span>sales@orlandbuildinggroup.com.au
    </div>
  </section>

  <section class="card card-back">
    <div class="back-rule"></div>
    <p class="back-url"><span>www.orlandbuildinggroup.com.au</span></p>
  </section>
</body>
</html>
```